Audio Visual Services Brochure for Direct Mailing

We are looking to design a direct mailing brochure detailing a new product that we are hoping to install in our immediate surrounding areas in London, UK. We are hoping for a half fold design, with a front page, two page centre spread and a rear page.
We have some very specific information that we want in the middle spread and want to tie this in for the front and rear pages.

Front Page Brief;
This page needs to deliver a problem that most modern households have in that they have too many remote controls (TV, DVD/Bluray, AV Reciever, Satellite TV, Plimmo TV, etc. etc.) We have taken a photo of this situation which may need to be improvded on.
We were hoping to design a page that presents this issue with text that backs up the photo along the lines of, "Does this look familiar? Too many remote controls and a complicated television system?". This page needs to grab the customer if they have this issue.

Centre Spread Brief;
This page presents two solutions to the first pages problem, A single room solution all in one remote control and a whole house solution which details how the system can scale to include lighting, multi-room audio distribution, cctv & security integration, HD/4K video distribution offering all of your video sources on all TV's in the property, Door entry, intercoms etc. etc.
This centre page has been taken from the manufacturers brochure and wants to be kept almost as is. We are very happy with this layout already.

Rear Page Brief;
Here we are hoping to provide a next step / contact us type of page with our company details, perhaps providing some company values and definitely pushing that we have been a SW20 local AV systems specialist since 2004.

Our website is at http://www.halvane-homeworks.co.uk which unfortunately still has our old company logo on it but this should help with services etc.

Any other questions please don't hesitate to get in contact.

Target Market(s)

Residential End User Homes - Mid to high income earners that can afford a £1K to £3K remote control system.

Industry/Entity Type

Audio

Font styles to use
Sans Serif

Colors

Designer to choose colors to be used in the design.

Requirements
Must have
• A catchy first page that entices the reader to open the brochure to see the middle section. Front page must be an attention grabber

```html
<!DOCTYPE html>
<html lang="en">
<head>
<meta charset="utf-8">
<title>Halvane Homeworks – Direct Mail Brochure</title>
<link href="https://fonts.googleapis.com/css2?family=Open+Sans:ital,wght@0,400;0,600;0,700;0,800;1,700&family=Oswald:wght@500;600&display=swap" rel="stylesheet">
<style>
  :root{
    --bg:#2a2a2c;
    --navy:#1f3f73;
    --blue:#2d5a94;
    --blue-mid:#3a6aa6;
    --blue-dark:#173259;
    --paper:#e9e9ea;
    --paper-shade:#cfd1d4;
    --ink:#3b3d42;
    --white:#ffffff;
    --badge:#8a9bb3;
    --charcoal:#3c3e42;
    --knit:#c9ad90;
    --knit-dark:#9c8068;
  }
  *{box-sizing:border-box;margin:0;padding:0}
  html,body{width:1200px;height:789px;overflow:hidden;background:var(--bg);font-family:"Open Sans",Arial,sans-serif}
  .canvas{position:relative;width:1200px;height:789px}
  .page{position:absolute;top:28px;width:520px;height:733px;overflow:hidden}
  .page--back{left:80px;background:linear-gradient(160deg,var(--paper) 0%,var(--paper-shade) 100%)}
  .page--front{left:600px;background:var(--navy)}
  .abs{position:absolute}

  /* back page */
  .back__photo{left:0;top:0;width:520px;height:580px;background:radial-gradient(ellipse at 30% 65%,#8fc9c6 0%,#b9c6cc 22%,#d9dadc 55%,#e6e6e7 100%)}
  .back__intro{left:34px;top:36px;width:440px;font-weight:700;font-size:17px;line-height:1.3;color:var(--ink)}
  .back__since{right:34px;top:148px;width:260px;text-align:right;font-weight:700;font-style:italic;font-size:16px;line-height:1.3;color:var(--navy)}
  .badge{left:400px;top:336px;width:80px;height:58px;border-radius:6px;background:var(--badge)}
  .back__brand{left:330px;top:410px;text-align:right;width:160px;color:var(--navy)}
  .brand-word{font-weight:800;font-size:30px;letter-spacing:1px;line-height:1}
  .brand-sub{font-weight:700;font-size:7px;letter-spacing:.6px;margin-top:4px}
  .back__band{left:0;top:0;width:520px;height:733px}
  .contact-tab{left:36px;top:548px;padding:8px 16px;background:var(--blue-mid);color:var(--white);font-weight:700;font-size:16px;letter-spacing:.5px}
  .contact{left:40px;top:598px;color:var(--white);font-size:11.5px;line-height:1.45}
  .contact__name{font-weight:700;margin-bottom:4px}
  .contact__row{display:flex;gap:8px;align-items:flex-start;margin-top:4px}
  .contact__row svg{flex:none;margin-top:2px}
  .contact__phone{font-weight:700}
  .social{left:300px;top:610px;display:flex;gap:10px}
  .social span{width:18px;height:18px;border-radius:50%;background:var(--white)}
  .back__web{left:300px;top:642px;color:var(--white);font-size:11.5px;display:flex;gap:6px;align-items:center}

  /* front page */
  .front__photo{left:0;top:30px;width:520px;height:500px;background:radial-gradient(ellipse at 55% 50%,#2b2b2e 0%,#56504a 18%,var(--knit-dark) 38%,var(--knit) 70%,#b89a7c 100%)}
  .front__shapes{left:0;top:0;width:520px;height:733px}
  .front__brand{left:150px;top:18px;display:flex;align-items:center;gap:12px;color:var(--white)}
  .front__brand .brand-word{font-size:38px}
  .front__brand .divider{width:1px;height:38px;background:var(--white)}
  .front__brand .brand-tag{font-weight:700;font-size:10px;line-height:1.15;letter-spacing:.8px}
  .tablet{left:340px;top:410px;width:130px;height:125px;background:linear-gradient(150deg,#5a6f90 0%,#2c3a52 60%,#1b2230 100%);border-radius:6px}
  .headline{left:28px;top:510px;color:var(--white);line-height:1.05}
  .headline__lead{font-weight:400;font-size:28px}
  .headline__main{font-weight:800;font-size:30px}
  .subline{left:30px;top:590px;color:var(--white);font-size:12.5px;line-height:1.45}
  .subline b{font-weight:700}
  .front__web{left:30px;top:650px;color:var(--white);font-size:11.5px;display:flex;gap:6px;align-items:center}
  .callnow{left:300px;top:584px;width:220px;height:40px;display:flex;align-items:center;justify-content:center;color:var(--white);font-family:"Oswald",Arial,sans-serif;font-weight:600;font-size:16px;letter-spacing:.3px}
</style>
</head>
<body>
<main class="canvas">

  <section class="page page--back" aria-label="Back page">
    <div class="abs back__photo" role="img" aria-label="Photo of an older woman in a teal top holding several remote controls in a bright living room"></div>

    <p class="abs back__intro">Halvane Homeworks is a specialist installer of Network Infrastructures &amp; Custom Audio Visual solutions.</p>
    <p class="abs back__since">We Have Been A Sw20 Local Av Systems Specialist Since 2004.</p>

    <div class="abs badge" aria-label="Authorised dealer badge"></div>
    <div class="abs back__brand">
      <div class="brand-word">HALVANE</div>
      <div class="brand-sub">HALVANE HOMEWORKS</div>
    </div>

    <svg class="abs back__band" viewBox="0 0 520 733" aria-hidden="true">
      <polygon points="0,578 520,500 520,733 0,733" fill="var(--navy)"/>
      <polygon points="270,548 520,510 520,733 270,733" fill="var(--blue-dark)"/>
      <polygon points="270,548 270,733 282,733 282,546" fill="var(--blue)" opacity=".6"/>
    </svg>

    <div class="abs contact-tab">CONTACT US</div>
    <div class="abs contact">
      <div class="contact__name">Halvane Homeworks Limited</div>
      <div class="contact__row">
        <svg width="10" height="13" viewBox="0 0 10 13"><path d="M5 0a5 5 0 0 0-5 5c0 3.5 5 8 5 8s5-4.5 5-8a5 5 0 0 0-5-5zm0 7a2 2 0 1 1 0-4 2 2 0 0 1 0 4z" fill="var(--white)"/></svg>
        <div>Ferncroft House<br>418 Alder Road<br>Larkfield Park<br>SW20 4QT</div>
      </div>
      <div class="contact__row">
        <svg width="11" height="11" viewBox="0 0 12 12"><circle cx="6" cy="6" r="5.2" fill="none" stroke="var(--white)" stroke-width="1.2"/><path d="M4 3.5l1 1.5-.6.7a4 4 0 0 0 1.9 1.9l.7-.6 1.5 1-.6 1A5 5 0 0 1 3 4.1z" fill="var(--white)"/></svg>
        <span class="contact__phone">0845 000 4471</span>
      </div>
      <div class="contact__row">
        <svg width="11" height="9" viewBox="0 0 12 9"><rect x=".5" y=".5" width="11" height="8" fill="none" stroke="var(--white)"/><path d="M.5.5l5.5 4.5L11.5.5" fill="none" stroke="var(--white)"/></svg>
        <span>sales@halvane-homeworks.co.uk</span>
      </div>
    </div>

    <div class="abs social" aria-label="Social media links"><span></span><span></span><span></span></div>
    <div class="abs back__web">
      <svg width="11" height="11" viewBox="0 0 12 12"><circle cx="6" cy="6" r="5.2" fill="none" stroke="var(--white)"/><ellipse cx="6" cy="6" rx="2.3" ry="5.2" fill="none" stroke="var(--white)"/><path d="M1 6h10" stroke="var(--white)"/></svg>
      <span>www.halvane-homeworks.co.uk</span>
    </div>
  </section>

  <section class="page page--front" aria-label="Front page">
    <div class="abs front__photo" role="img" aria-label="Photo of hands in a knitted jumper holding a bundle of black and white remote controls"></div>

    <svg class="abs front__shapes" viewBox="0 0 520 733" aria-hidden="true">
      <polygon points="0,0 520,0 520,40 120,100 0,90" fill="var(--navy)"/>
      <polygon points="0,60 120,100 0,100" fill="var(--blue-dark)"/>
      <polygon points="0,520 520,440 520,733 0,733" fill="var(--navy)"/>
      <polygon points="0,520 300,474 300,486 0,532" fill="var(--blue-mid)" opacity=".8"/>
      <polygon points="290,600 520,566 520,733 290,733" fill="var(--blue-dark)" opacity=".5"/>
      <polygon points="300,596 520,562 520,618 300,652" fill="var(--charcoal)"/>
    </svg>

    <div class="abs front__brand">
      <div class="brand-word">HALVANE</div>
      <div class="divider"></div>
      <div class="brand-tag">HALVANE<br>HOMEWORKS<br>LONDON</div>
    </div>

    <div class="abs tablet" role="img" aria-label="Photo of a wall-mounted touchscreen control panel"></div>

    <div class="abs headline">
      <div class="headline__lead">DOES THIS</div>
      <div class="headline__main">LOOK FAMILIAR?</div>
    </div>
    <p class="abs subline">Too many <b>REMOTE CONTROLS</b> and a<br>Complicated Television System?</p>
    <div class="abs front__web">
      <svg width="11" height="11" viewBox="0 0 12 12"><circle cx="6" cy="6" r="5.2" fill="none" stroke="var(--white)"/><ellipse cx="6" cy="6" rx="2.3" ry="5.2" fill="none" stroke="var(--white)"/><path d="M1 6h10" stroke="var(--white)"/></svg>
      <span>www.halvane-homeworks.co.uk</span>
    </div>
    <div class="abs callnow">CALL NOW - 0845 000 4471</div>
  </section>

</main>
</body>
</html>
```